BuildLinkage.com Full Stationery Design

Business Card will have all info on it. Letterhead will not have name, title or mobile number. Keep general feeling very clean, using colors from the logo as accents.
Name:Dale Vanterpool
Title:President
Phone: 1-800-555-4926
Cell: 306-555-7312
email: dale@buildlinkage.com
website: www.buildlinkage.com
Address:
PO Box 874
Brennick, SK
S0M2T7

Target Market(s)

Construction Business owners

Industry/Entity Type

Business

Contact Information for Business Card

Name:Dale Vanterpool
Title:President
Phone: 1-800-555-4926
Cell: 306-555-7312
Address:
PO Box 874
Brennick, SK
S0M2T7

Font styles to use
Sans Serif

Requirements
Must have
• Clean look
Should not have
• Images or cartoon type characters or tools

```html
<!DOCTYPE html>
<html lang="en">
<head>
<meta charset="utf-8">
<title>BuildLinkage.com Stationery</title>
<link href="https://fonts.googleapis.com/css2?family=Open+Sans:wght@400;600&display=swap" rel="stylesheet">
<style>
  :root {
    --bg: #e5e5e5;
    --paper: #ffffff;
    --slate: #4d5b6e;
    --slate-light: #6b7d90;
    --red: #e8262f;
    --orange: #f7941d;
    --ink: #333a44;
  }
  * { margin: 0; padding: 0; box-sizing: border-box; }
  html, body { width: 1200px; height: 1200px; overflow: hidden; }
  body {
    background: var(--bg);
    font-family: "Open Sans", Arial, sans-serif;
    color: var(--ink);
    position: relative;
  }
  .sheet { position: absolute; background: var(--paper); overflow: hidden; }

  .brand { display: flex; align-items: center; gap: 6px; white-space: nowrap; }
  .brand-mark { background: var(--orange); flex: none; }
  .brand-name { font-weight: 600; color: var(--slate); }

  .footer-bar {
    position: absolute; left: 0; right: 0; bottom: 0;
    background: linear-gradient(90deg, var(--red), var(--orange));
  }
  .footer-url {
    position: absolute; top: 0; bottom: 0; right: 0;
    background: var(--slate-light);
    color: #fff;
    display: flex; align-items: center; justify-content: center;
    white-space: nowrap;
  }
  .footer-gap { position: absolute; top: 0; bottom: 0; right: 0; background: #fff; }

  .info-row { display: flex; align-items: center; gap: 3px; white-space: nowrap; }
  .icon { width: 6px; height: 6px; flex: none; }

  /* Letterhead */
  .letterhead { left: 178px; top: 210px; width: 384px; height: 542px; }
  .letterhead .brand { position: absolute; left: 26px; top: 47px; }
  .letterhead .brand-mark { width: 14px; height: 14px; }
  .letterhead .brand-name { font-size: 13px; }
  .letterhead .contact-block {
    position: absolute; left: 260px; top: 34px;
    border-left: 1px solid #ccc; padding-left: 5px;
    font-size: 6px; line-height: 8px; white-space: nowrap;
  }
  .letterhead .footer-bar { height: 14px; }

  /* Folder */
  .folder { left: 624px; top: 187px; width: 458px; height: 567px; }
  .folder .brand { position: absolute; left: 0; right: 0; top: 165px; justify-content: center; gap: 10px; }
  .folder .brand-mark { width: 40px; height: 40px; }
  .folder .brand-name { font-size: 34px; }
  .folder .footer-bar { height: 13px; }

  /* Business card front */
  .card-front { left: 40px; top: 798px; width: 174px; height: 100px; }
  .card-front .brand { position: absolute; left: 9px; top: 15px; gap: 4px; }
  .card-front .brand-mark { width: 10px; height: 10px; }
  .card-front .brand-name { font-size: 9px; }
  .card-front .person {
    position: absolute; right: 10px; top: 54px; text-align: right;
    border-bottom: 1px solid #ddd; width: 154px; padding-bottom: 1px;
  }
  .person .name { font-size: 6px; font-weight: 600; color: var(--slate); line-height: 7px; }
  .person .title { font-size: 4px; color: var(--red); line-height: 5px; }
  .card-front .card-contact { position: absolute; left: 10px; top: 71px; font-size: 4px; line-height: 5.5px; }
  .card-contact .icon { width: 3px; height: 3px; }
  .card-front .card-address { position: absolute; right: 10px; top: 78px; font-size: 4px; line-height: 5px; text-align: right; white-space: nowrap; }
  .card-front .footer-bar { height: 6px; }
  .card-front .footer-url { font-size: 3.5px; }

  /* Business card back */
  .card-back {
    left: 41px; top: 922px; width: 174px; height: 100px;
    background: linear-gradient(90deg, var(--slate), var(--slate-light));
    display: flex; align-items: center; justify-content: center;
  }
  .card-back .brand-mark { width: 14px; height: 14px; }
  .card-back .brand-name { font-size: 11px; color: #fff; }

  /* Envelope front */
  .envelope { left: 257px; top: 813px; width: 429px; height: 204px; }
  .envelope .brand { position: absolute; left: 15px; top: 31px; }
  .envelope .brand-mark { width: 14px; height: 14px; }
  .envelope .brand-name { font-size: 13px; }
  .envelope .return-address { position: absolute; left: 15px; top: 164px; font-size: 6.5px; line-height: 8px; }
  .envelope .footer-bar { height: 14px; }

  /* Envelope back */
  .envelope-back { left: 722px; top: 813px; width: 431px; height: 204px; }
  .envelope-back svg { position: absolute; left: 0; top: 0; }
</style>
</head>
<body>

  <section class="sheet letterhead" aria-label="Letterhead">
    <div class="brand"><span class="brand-mark"></span><span class="brand-name">BuildLinkage.com</span></div>
    <div class="contact-block">
      <div>PO Box 874 Brennick,</div>
      <div>SKS0M2T7</div>
      <div class="info-row" style="margin-top:2px">
        <svg class="icon" viewBox="0 0 10 10"><path d="M2 1h2l1 2-1.5 1a5 5 0 0 0 2.5 2.5L7 5l2 1v2c-4 1-8-3-7-7z" fill="#e8262f"/></svg>1-800-555-4926
      </div>
      <div class="info-row">
        <svg class="icon" viewBox="0 0 10 10"><rect x="1" y="2" width="8" height="6" fill="#e8262f"/><path d="M1 2l4 3 4-3" stroke="#fff" fill="none"/></svg>dale@buildlinkage.com
      </div>
    </div>
    <div class="footer-bar">
      <div class="footer-gap" style="width:154px;clip-path:polygon(14px 0,100% 0,100% 100%,0 100%)"></div>
      <div class="footer-url" style="width:148px;clip-path:polygon(14px 0,100% 0,100% 100%,0 100%);font-size:7px">www.buildlinkage.com</div>
    </div>
  </section>

  <section class="sheet folder" aria-label="Presentation folder">
    <div class="brand"><span class="brand-mark"></span><span class="brand-name">BuildLinkage.com</span></div>
    <div class="footer-bar">
      <div class="footer-gap" style="width:172px;clip-path:polygon(13px 0,100% 0,100% 100%,0 100%)"></div>
      <div class="footer-url" style="width:166px;clip-path:polygon(13px 0,100% 0,100% 100%,0 100%);font-size:7px">www.buildlinkage.com</div>
    </div>
  </section>

  <section class="sheet card-front" aria-label="Business card front">
    <div class="brand"><span class="brand-mark"></span><span class="brand-name">BuildLinkage.com</span></div>
    <div class="person">
      <div class="name">Dale Vanterpool</div>
      <div class="title">President</div>
    </div>
    <div class="card-contact">
      <div class="info-row"><svg class="icon" viewBox="0 0 10 10"><path d="M2 1h2l1 2-1.5 1a5 5 0 0 0 2.5 2.5L7 5l2 1v2c-4 1-8-3-7-7z" fill="#e8262f"/></svg>1-800-555-4926</div>
      <div class="info-row"><svg class="icon" viewBox="0 0 10 10"><rect x="3" y="1" width="4" height="8" rx="1" fill="#e8262f"/></svg>306-555-7312</div>
      <div class="info-row"><svg class="icon" viewBox="0 0 10 10"><rect x="1" y="2" width="8" height="6" fill="#e8262f"/></svg>dale@buildlinkage.com</div>
    </div>
    <div class="card-address">PO Box 874 Brennick,<br>SKS0M2T7</div>
    <div class="footer-bar">
      <div class="footer-gap" style="width:76px;clip-path:polygon(6px 0,100% 0,100% 100%,0 100%)"></div>
      <div class="footer-url" style="width:73px;clip-path:polygon(6px 0,100% 0,100% 100%,0 100%)">www.buildlinkage.com</div>
    </div>
  </section>

  <section class="sheet card-back" aria-label="Business card back">
    <div class="brand"><span class="brand-mark"></span><span class="brand-name">BuildLinkage.com</span></div>
  </section>

  <section class="sheet envelope" aria-label="Envelope front">
    <div class="brand"><span class="brand-mark"></span><span class="brand-name">BuildLinkage.com</span></div>
    <div class="return-address">PO Box 874 Brennick,<br>SKS0M2T7</div>
    <div class="footer-bar">
      <div class="footer-gap" style="width:164px;clip-path:polygon(14px 0,100% 0,100% 100%,0 100%)"></div>
      <div class="footer-url" style="width:158px;clip-path:polygon(14px 0,100% 0,100% 100%,0 100%);font-size:7.5px">www.buildlinkage.com</div>
    </div>
  </section>

  <section class="sheet envelope-back" aria-label="Envelope back">
    <svg width="431" height="204" viewBox="0 0 431 204">
      <defs>
        <linearGradient id="flap" x1="0" x2="1">
          <stop offset="0" stop-color="#4d5b6e"/>
          <stop offset="1" stop-color="#6b7d90"/>
        </linearGradient>
      </defs>
      <path d="M0 0H431L424 60Q422 70 410 70H21Q9 70 7 60Z" fill="url(#flap)"/>
      <rect x="205" y="24" width="20" height="20" fill="#f7941d"/>
    </svg>
  </section>

</body>
</html>
```